Modern Innovative Business Card Design

We require a nice, modern, clean business card design, ready for upload to Cardwello. Our company develops online banking software solutions for small financial insitutions. The design should be clean, professional, but yet not "corporate boring". See www.fintrola.com for an idea of business image and profile. The design should communicate innovation, be modern and fresh, yet look professional and established.

Target Market(s)

Finance industry, bankers, entrepreneurs

Industry/Entity Type

Financial

Contact Information for Business Card

Daniel Hargreave
CEO

FINTROLA BV
Lindenhofstraat 38
1072 KD Amsterdam
The Netherlands

Phone: +31 20 517 8063
Direct: +31 20 446 1975
Skype: daniel.fintrola
ceo@fintrola.com
www.fintrola.com

Font styles to use
Sans Serif

Requirements
Must have
• Should look clean, modern and professional. File should be ready for upload to cardwello.
Should not have
• Boring standard corporate layout

```html
<!DOCTYPE html>
<html lang="en">
<head>
<meta charset="utf-8">
<title>Fintrola Business Card</title>
<link href="https://fonts.googleapis.com/css2?family=Ubuntu:wght@400;500;700&display=swap" rel="stylesheet">
<style>
  :root {
    --bg: #e6e4e0;
    --card: #0c0c0c;
    --green: #8fc73e;
    --grey: #8a8a8a;
    --grey-dark: #6b6b6b;
  }
  * { margin: 0; padding: 0; box-sizing: border-box; }
  html, body { width: 1200px; height: 900px; overflow: hidden; background: var(--bg); }
  body { position: relative; font-family: "Ubuntu", sans-serif; }

  .business-card {
    position: absolute; left: 150px; top: 180px;
    width: 900px; height: 540px;
    background: var(--card);
    border-radius: 32px;
    overflow: hidden;
  }
  .brand {
    position: absolute; left: 62px; top: 92px;
    display: flex; align-items: center; gap: 18px;
  }
  .brand-square { width: 26px; height: 26px; background: var(--green); }
  .brand-name {
    font-size: 74px; font-weight: 500; letter-spacing: 2px;
    color: var(--grey-dark); line-height: 1;
  }
  .person {
    position: absolute; right: 62px; top: 168px; text-align: right;
  }
  .person-name { font-size: 30px; font-weight: 700; color: var(--green); }
  .person-role { font-size: 20px; color: var(--grey-dark); margin-top: 2px; }
  .divider {
    position: absolute; left: 100px; right: 62px; top: 245px;
    height: 2px; background: var(--green);
  }
  .contact-list {
    position: absolute; right: 62px; top: 278px;
    list-style: none; text-align: right;
  }
  .contact-list li {
    display: flex; justify-content: flex-end; align-items: center; gap: 12px;
    font-size: 22px; color: var(--grey); height: 27px; letter-spacing: 0.5px;
  }
  .contact-list svg { width: 20px; height: 20px; flex: none; }
  .address {
    position: absolute; left: 62px; top: 365px;
    font-size: 22px; line-height: 28px; color: var(--grey-dark); font-style: normal;
  }
  .address-company { font-weight: 700; color: var(--green); }
  .accent-band {
    position: absolute; left: 0; right: 0; bottom: 0; height: 62px;
    background: var(--green);
  }
</style>
</head>
<body>
  <div class="business-card">
    <div class="brand">
      <span class="brand-name">FINTROLA</span>
      <span class="brand-square"></span>
    </div>

    <div class="person">
      <div class="person-name">Daniel Hargreave</div>
      <div class="person-role">CEO</div>
    </div>

    <div class="divider"></div>

    <ul class="contact-list">
      <li>+31 20 517 8063
        <svg viewBox="0 0 20 20" aria-hidden="true"><path d="M5 2l3 4-2 2c1 2 3 4 5 5l2-2 4 3-2 3C9 17 3 11 2 5z" fill="var(--green)"/></svg>
      </li>
      <li>+31 20 446 1975
        <svg viewBox="0 0 20 20" aria-hidden="true"><path d="M5 2l3 4-2 2c1 2 3 4 5 5l2-2 4 3-2 3C9 17 3 11 2 5z" fill="var(--green)"/></svg>
      </li>
      <li>ceo@fintrola.com
        <svg viewBox="0 0 20 20" aria-hidden="true"><rect x="1" y="4" width="18" height="12" fill="var(--green)"/><path d="M1 4l9 7 9-7" stroke="var(--card)" stroke-width="1.5" fill="none"/></svg>
      </li>
      <li>daniel.fintrola
        <svg viewBox="0 0 20 20" aria-hidden="true"><circle cx="10" cy="10" r="9" fill="var(--green)"/></svg>
      </li>
      <li>www.fintrola.com
        <svg viewBox="0 0 20 20" aria-hidden="true"><circle cx="10" cy="10" r="9" fill="var(--green)"/><path d="M1 10h18M10 1c-4 5-4 13 0 18M10 1c4 5 4 13 0 18" stroke="var(--card)" stroke-width="1.3" fill="none"/></svg>
      </li>
    </ul>

    <address class="address">
      <div class="address-company">FINTROLA BV</div>
      Lindenhofstraat 38,<br>
      1072 KD Amsterdam,<br>
      The Netherlands
    </address>

    <div class="accent-band"></div>
  </div>
</body>
</html>
```